Brindle Works Business Card

We need a business card design for an existing company (www.brindle-works.example). The business cards will be by Pavo in their Velta range (http://uk.pavoprint.example/products/velta/business-cards.html).

The card should be landscape, with the full company logo on the reverse side. I would like to have the card to portray a professional image (this is a high technology niche consultancy company). The card should be mostly white but aligned with our website (this is mostly dark colours). I can supply the logo files etc.

Details on the card should include the following:

Name (example: Martin Oakbury)
Position (example: Principal Consultant)
Email Address (example: martin@brindle-works.example)
Mobile Phone Number (example: +44 (0) 7912 604 385)
Website (example: www.brindle-works.example)
Twitter (example: @brindleworksco)
Facebook (example: www.facebook.com/brindleworksco)

I would like the text on the front of the card to be black. Thanks.

Industry/Entity Type

Business

Requirements
Should not have
• The company address on the card.

```html
<!DOCTYPE html>
<html lang="en">
<head>
<meta charset="utf-8">
<title>Brindle Works Business Card</title>
<link href="https://fonts.googleapis.com/css2?family=Open+Sans:wght@400;600;700&display=swap" rel="stylesheet">
<style>
  :root {
    --orange: #f26a1b;
    --charcoal: #232323;
    --band-grey: #4a4a4a;
    --pill-grey: #555555;
    --paper: #e3e4e5;
    --white: #ffffff;
    --ink: #111111;
    --tagline: #444444;
    --backdrop: #d9d4cc;
  }
  * { margin: 0; padding: 0; box-sizing: border-box; }
  html, body { width: 1200px; height: 916px; overflow: hidden; }
  body {
    background: var(--backdrop);
    font-family: "Open Sans", Arial, sans-serif;
    position: relative;
  }
  .card {
    position: absolute;
    width: 620px;
    height: 356px;
    overflow: hidden;
    box-shadow: 0 6px 18px rgba(0,0,0,0.25);
  }
  .band {
    position: absolute; left: 0; right: 0; height: 10px;
    background: var(--band-grey);
  }
  .band--top { top: 0; }
  .band--bottom { bottom: 0; }
  .band__accent {
    position: absolute; top: 0; height: 12px; width: 170px;
    background: var(--orange);
  }
  .band--bottom .band__accent { top: -2px; }

  /* Front */
  .card--front { left: 150px; top: 90px; background: var(--charcoal); }
  .card--front .band__accent { left: 185px; }
  .contact {
    position: absolute; left: 78px; top: 92px;
    display: grid; grid-template-columns: 70px 14px auto;
    row-gap: 2px; font-size: 14px; line-height: 19px;
  }
  .contact__label { color: var(--white); }
  .contact__sep { color: var(--white); }
  .contact__value { color: var(--orange); font-weight: 600; }
  .front-mark {
    position: absolute; left: 425px; top: 150px;
    width: 70px; height: 70px; border-radius: 50%;
    background: var(--orange);
  }
  .role-bar {
    position: absolute; left: 395px; top: 232px; width: 240px; height: 34px;
    background: var(--orange); border-radius: 17px 0 0 17px;
    color: var(--ink); font-weight: 700; font-size: 15px;
    line-height: 34px; padding-left: 26px;
  }
  .name-pill {
    position: absolute; left: 135px; top: 270px; width: 290px; height: 32px;
    background: var(--pill-grey); border-radius: 16px;
    color: var(--white); font-size: 19px; letter-spacing: 1.5px;
    line-height: 32px; padding-left: 18px;
  }

  /* Back */
  .card--back { left: 430px; top: 470px; background: var(--paper); }
  .card--back .band--top .band__accent { left: 200px; }
  .card--back .band--bottom .band__accent { left: 290px; }
  .brand {
    position: absolute; left: 70px; top: 128px;
    display: flex; align-items: center; gap: 26px;
  }
  .brand__dot {
    width: 92px; height: 92px; border-radius: 50%;
    background: var(--orange); flex: none;
  }
  .brand__name {
    color: var(--orange); font-weight: 700; font-size: 25px;
    letter-spacing: 1px; text-transform: uppercase; line-height: 1.1;
    white-space: nowrap;
  }
  .brand__tagline {
    color: var(--tagline); font-size: 16px; letter-spacing: 1px; margin-top: 6px;
    white-space: nowrap;
  }
</style>
</head>
<body>
  <section class="card card--front" aria-label="Card front">
    <div class="band band--top"><span class="band__accent"></span></div>
    <div class="contact">
      <span class="contact__label">Email</span><span class="contact__sep">:</span><span class="contact__value">martin@brindle-works.example</span>
      <span class="contact__label">Mobile</span><span class="contact__sep">:</span><span class="contact__value">+44 (0) 7912 604 385</span>
      <span class="contact__label">Website</span><span class="contact__sep">:</span><span class="contact__value">www.brindle-works.example</span>
      <span class="contact__label">Twitter</span><span class="contact__sep">:</span><span class="contact__value">@brindleworksco</span>
      <span class="contact__label">Facebook</span><span class="contact__sep">:</span><span class="contact__value">www.facebook.com/brindleworksco</span>
    </div>
    <div class="front-mark" aria-hidden="true"></div>
    <div class="role-bar">Principal Consultant</div>
    <div class="name-pill">MARTIN OAKBURY</div>
  </section>

  <section class="card card--back" aria-label="Card back">
    <div class="band band--top"><span class="band__accent"></span></div>
    <div class="brand">
      <span class="brand__dot" aria-hidden="true"></span>
      <div>
        <div class="brand__name">Brindle Works Solutions</div>
        <div class="brand__tagline">Smart Systems - Clear Advice - Real Value</div>
      </div>
    </div>
    <div class="band band--bottom"><span class="band__accent"></span></div>
  </section>
</body>
</html>
```